Property Auctions with Gareth Whitlow

Podcast cover art 3000px by 3000px. Eye catching for a weekly podcast. The words should read Property Auctions (large font) with Gareth Whitlow (smaller font)

I would like the font and colours to be similar to my book, a copy of which I have attached.

Target Market(s)

New and experienced property investors looking to purchase at a property auction

```html
<!DOCTYPE html>
<html lang="en">
<head>
<meta charset="utf-8">
<title>Property Auctions with Gareth Whitlow</title>
<link rel="stylesheet" href="https://fonts.googleapis.com/css2?family=Roboto+Condensed:wght@700;900&display=swap">
<style>
  :root {
    --bg-deep: #121a1e;
    --bg-mid: #2b3840;
    --bg-glow: #5a646a;
    --gold-dark: #a8742a;
    --gold-mid: #d7ad4f;
    --gold-light: #f6e48c;
    --house-black: #1c1c1c;
    --photo-light: #8a9297;
    --photo-mid: #4e575c;
    --white: #ffffff;
  }
  html, body {
    margin: 0;
    padding: 0;
    width: 1200px;
    height: 1200px;
    overflow: hidden;
    background: var(--bg-deep);
  }
  .cover {
    display: block;
    width: 1200px;
    height: 1200px;
  }
  .title-text,
  .host-text,
  .with-text,
  .pound-sign {
    font-family: "Roboto Condensed", "Arial Narrow", sans-serif;
    font-weight: 900;
  }
  .host-text { letter-spacing: 2px; }
  .with-text { fill: var(--white); }
</style>
</head>
<body>
<svg class="cover" viewBox="0 0 1200 1200" xmlns="http://www.w3.org/2000/svg">
  <defs>
    <radialGradient id="bgGlow" cx="0.5" cy="0.48" r="0.65">
      <stop offset="0" stop-color="var(--bg-glow)"/>
      <stop offset="0.45" stop-color="var(--bg-mid)"/>
      <stop offset="1" stop-color="var(--bg-deep)"/>
    </radialGradient>
    <linearGradient id="goldFill" x1="0" y1="0" x2="1" y2="0.15">
      <stop offset="0" stop-color="var(--gold-dark)"/>
      <stop offset="0.18" stop-color="var(--gold-mid)"/>
      <stop offset="0.35" stop-color="var(--gold-light)"/>
      <stop offset="0.55" stop-color="var(--gold-mid)"/>
      <stop offset="0.72" stop-color="var(--gold-light)"/>
      <stop offset="0.88" stop-color="var(--gold-mid)"/>
      <stop offset="1" stop-color="var(--gold-dark)"/>
    </linearGradient>
    <radialGradient id="photoTone" cx="0.45" cy="0.5" r="0.55">
      <stop offset="0" stop-color="var(--photo-light)" stop-opacity="0.75"/>
      <stop offset="0.55" stop-color="var(--photo-mid)" stop-opacity="0.5"/>
      <stop offset="1" stop-color="var(--photo-mid)" stop-opacity="0"/>
    </radialGradient>
    <radialGradient id="houseTone" cx="0.5" cy="0.55" r="0.6">
      <stop offset="0" stop-color="var(--gold-mid)" stop-opacity="0.55"/>
      <stop offset="0.35" stop-color="var(--house-black)" stop-opacity="0.95"/>
      <stop offset="0.8" stop-color="var(--house-black)" stop-opacity="0.7"/>
      <stop offset="1" stop-color="var(--house-black)" stop-opacity="0"/>
    </radialGradient>
    <radialGradient id="lensFlare" cx="0.5" cy="0.5" r="0.5">
      <stop offset="0" stop-color="#ffffff" stop-opacity="0.95"/>
      <stop offset="0.3" stop-color="#f3d9ff" stop-opacity="0.45"/>
      <stop offset="1" stop-color="#ffffff" stop-opacity="0"/>
    </radialGradient>
    <filter id="textShadow" x="-5%" y="-5%" width="110%" height="120%">
      <feDropShadow dx="0" dy="6" stdDeviation="8" flood-color="#000" flood-opacity="0.55"/>
    </filter>
  </defs>

  <rect class="background" width="1200" height="1200" fill="url(#bgGlow)"/>

  <rect class="photo-area" x="0" y="480" width="560" height="420"
        fill="url(#photoTone)" role="img"
        aria-label="Greyscale photo of hands placing a SOLD sticker over a home for sale sign"/>

  <rect class="house-icon-area" x="60" y="650" width="720" height="550"
        fill="url(#houseTone)" role="img"
        aria-label="Black and gold house shape with an upward arrow inside"/>

  <g class="podcast-title" filter="url(#textShadow)">
    <text class="title-text" x="102" y="298" font-size="290" fill="url(#goldFill)"
          textLength="997" lengthAdjust="spacingAndGlyphs">PROPERTY</text>
    <text class="title-text" x="118" y="522" font-size="290" fill="url(#goldFill)"
          textLength="957" lengthAdjust="spacingAndGlyphs">AUCTIONS</text>
  </g>

  <circle class="title-glint" cx="405" cy="108" r="42" fill="url(#lensFlare)"/>

  <g class="host-block" filter="url(#textShadow)">
    <text class="with-text" x="770" y="612" font-size="66"
          textLength="130" lengthAdjust="spacingAndGlyphs">with</text>
    <text class="host-text" x="630" y="720" font-size="104" fill="url(#goldFill)"
          textLength="430" lengthAdjust="spacingAndGlyphs">GARETH</text>
    <text class="host-text" x="636" y="826" font-size="110" fill="url(#goldFill)"
          textLength="430" lengthAdjust="spacingAndGlyphs">WHITLOW</text>
  </g>

  <text class="pound-sign" x="818" y="1098" font-size="230" fill="url(#goldFill)"
        filter="url(#textShadow)">£</text>
</svg>
</body>
</html>
```